Harbourline Gas and Plumbing Business Card Design

I am after a business card design for my plumbing business called 'Harbourline Gas & Plumbing'. I do all types of plumbing and gas work and specialise in general maintenance plumbing. Would like to see designs using current logo

Industry/Entity Type

Plumbing

Contact Information for Business Card

Name - Dalton McKendry
Phone number - 0438561027
Email - admin@harbourlinegasplumbing.example
ABN - 58204936115

```html
<!DOCTYPE html>
<html lang="en">
<head>
<meta charset="utf-8">
<title>Harbourline Gas &amp; Plumbing – Business Card</title>
<link rel="stylesheet" href="https://fonts.googleapis.com/css2?family=Orbitron:wght@700;800;900&family=Roboto:wght@400;500&display=swap">
<style>
  :root {
    --stage: #141414;
    --brand-blue: #2a55b8;
    --deep-blue: #2d46a8;
    --sun-yellow: #f9cc22;
    --flame-orange: #f28a2e;
    --ink: #1d1d1d;
    --rule: #3a3a3a;
    --paper: #ffffff;
  }
  * { box-sizing: border-box; margin: 0; padding: 0; }
  html, body { width: 1200px; height: 1200px; overflow: hidden; background: var(--stage); }
  .stage {
    width: 1200px; height: 1200px;
    display: flex; flex-direction: column; align-items: center; justify-content: center; gap: 60px;
  }
  .card {
    width: 960px; height: 520px; border-radius: 34px; position: relative; overflow: hidden;
  }

  /* Back face */
  .card--back {
    background: linear-gradient(180deg, var(--sun-yellow) 0%, #b8b46a 18%, #4f7fc4 40%, #2f62bf 60%, var(--deep-blue) 100%);
    color: var(--paper);
  }
  .card--back .wordmark {
    position: absolute; top: 160px; left: 80px; right: 80px; text-align: center;
    font-family: "Orbitron", sans-serif; font-weight: 900; font-size: 40px; line-height: 1.2;
    letter-spacing: 1px; color: var(--paper);
  }
  .card--back .tagline {
    position: absolute; bottom: 70px; left: 70px; right: 70px; text-align: center;
    font-family: "Orbitron", sans-serif; font-weight: 700; font-size: 16px; line-height: 1.5;
    letter-spacing: 0.5px; text-transform: uppercase;
  }

  /* Front face */
  .card--front { background: var(--paper); color: var(--ink); }
  .card--front .wordmark {
    position: absolute; top: 64px; left: 70px;
    font-family: "Orbitron", sans-serif; font-weight: 900; font-size: 42px; line-height: 1.15;
    letter-spacing: 1px; color: var(--brand-blue);
  }
  .brand-dot {
    position: absolute; top: 130px; right: 110px; width: 200px; height: 200px; border-radius: 50%;
    background: var(--flame-orange);
  }
  .contact-name {
    position: absolute; top: 300px; left: 70px;
    font-family: "Orbitron", sans-serif; font-weight: 800; font-size: 28px; letter-spacing: 0.5px;
    color: var(--brand-blue); text-transform: uppercase;
  }
  .abn {
    position: absolute; top: 346px; left: 70px;
    font-family: "Roboto", sans-serif; font-size: 24px; color: var(--ink);
  }
  .abn .label { color: var(--deep-blue); font-weight: 500; }
  .contact-rule {
    position: absolute; top: 390px; left: 70px; right: 70px; height: 2px; background: var(--rule);
  }
  .contact-row {
    position: absolute; display: flex; align-items: center; gap: 14px;
    font-family: "Roboto", sans-serif; font-size: 24px; color: var(--ink);
  }
  .contact-row--phone { top: 408px; left: 70px; }
  .contact-row--email { bottom: 40px; right: 70px; }
  .contact-row svg { width: 30px; height: 30px; flex: none; }
</style>
</head>
<body>
<main class="stage">
  <section class="card card--back">
    <div class="wordmark">HARBOURLINE<br>GAS &amp; PLUMBING</div>
    <p class="tagline">All types of plumbing and gas work and specialise in<br>general maintenance plumbing</p>
  </section>

  <section class="card card--front">
    <div class="wordmark">HARBOURLINE<br>GAS &amp; PLUMBING</div>
    <div class="brand-dot"></div>

    <div class="contact-name">Dalton McKendry</div>
    <div class="abn"><span class="label">ABN</span> - 58204936115</div>
    <div class="contact-rule"></div>

    <div class="contact-row contact-row--phone">
      <svg viewBox="0 0 30 30" aria-hidden="true">
        <rect width="30" height="30" rx="4" fill="#2a55b8"/>
        <path d="M10 7c1 0 2 2.5 2.5 3.5s-1.5 2-1 3c1 2 3 4 5 5 1 .5 2-1.5 3-1s3.5 1.5 3.5 2.5-1.5 3-3.5 3C13 23 7 17 7 11c0-2 2-4 3-4z" fill="#fff"/>
      </svg>
      <span>0438561027</span>
    </div>

    <div class="contact-row contact-row--email">
      <svg viewBox="0 0 30 30" aria-hidden="true">
        <rect width="30" height="30" rx="4" fill="#2a55b8"/>
        <rect x="6" y="9" width="18" height="12" fill="none" stroke="#fff" stroke-width="1.8"/>
        <path d="M6 9l9 7 9-7" fill="none" stroke="#fff" stroke-width="1.8"/>
      </svg>
      <span>admin@harbourlinegasplumbing.example</span>
    </div>
  </section>
</main>
</body>
</html>
```